STAND OUT BUSINESS CARD REQUIRED

I would like a business card that is going to be different and stand out!

Target Market(s)

Residential market, adults from 28yrs on

Industry/Entity Type

Electrician

Requirements
Must have
• Business name
• my name
• phone number
• email
• web address
• license no.
• abn
• fax no
• logo
Nice to have
• Extra info:
• FREE quotes
• Fixed pricing
• On time guarantee
• Life time labour Guarantee

```html
<!DOCTYPE html>
<html lang="en">
<head>
<meta charset="utf-8">
<title>Bright Spark Electrical – Business Card</title>
<link rel="stylesheet" href="https://fonts.googleapis.com/css2?family=Michroma&display=swap">
<style>
  :root {
    --navy: #1c1c7a;
    --shadow: rgba(60, 60, 60, 0.45);
    --yellow-light: #fffde0;
    --yellow: #f6ee3a;
    --yellow-edge: #e8dc12;
    --paper: #ffffff;
  }
  * { margin: 0; padding: 0; box-sizing: border-box; }
  html, body { width: 1200px; height: 720px; overflow: hidden; background: var(--paper); }
  .card {
    position: relative;
    width: 1200px;
    height: 720px;
    background: var(--paper);
    font-family: "Michroma", sans-serif;
    color: var(--navy);
  }
  .brand-mark {
    position: absolute;
    left: 56px;
    top: 60px;
    width: 230px;
    display: flex;
    flex-direction: column;
    align-items: flex-start;
    gap: 14px;
  }
  .brand-mark__dot {
    width: 54px;
    height: 54px;
    border-radius: 50%;
    background: var(--navy);
  }
  .brand-mark__name {
    font-size: 22px;
    line-height: 1.35;
    color: var(--navy);
  }
  .contact {
    position: absolute;
    left: 630px;
    top: 36px;
    list-style: none;
  }
  .contact li {
    font-size: 37px;
    line-height: 46px;
    letter-spacing: 1px;
    text-shadow: 3px 3px 3px var(--shadow);
  }
  .banner {
    position: absolute;
    left: 0;
    top: 0;
    width: 1200px;
    height: 720px;
  }
  .banner__title {
    position: absolute;
    left: 0;
    width: 1200px;
    top: 572px;
    text-align: center;
    font-size: 37px;
    letter-spacing: 1px;
    text-shadow: 3px 3px 3px var(--shadow);
  }
  .banner__tagline {
    position: absolute;
    left: 0;
    width: 1200px;
    top: 646px;
    text-align: center;
    font-size: 15px;
    letter-spacing: 0.5px;
  }
</style>
</head>
<body>
  <main class="card">
    <div class="brand-mark">
      <span class="brand-mark__dot"></span>
      <span class="brand-mark__name">BRIGHT SPARK<br>ELECTRICAL</span>
    </div>

    <ul class="contact">
      <li>NAME</li>
      <li>ADDRESS</li>
      <li>ADDRESS</li>
      <li>PHONE</li>
      <li>E.MAIL</li>
    </ul>

    <svg class="banner" viewBox="0 0 1200 720" aria-hidden="true">
      <defs>
        <linearGradient id="bannerFill" x1="0" y1="0" x2="0" y2="1">
          <stop offset="0" stop-color="var(--yellow-light)"/>
          <stop offset="0.55" stop-color="var(--yellow)"/>
          <stop offset="1" stop-color="var(--yellow)"/>
        </linearGradient>
        <filter id="bannerShadow" x="-5%" y="-5%" width="110%" height="120%">
          <feDropShadow dx="4" dy="6" stdDeviation="5" flood-color="#555" flood-opacity="0.45"/>
        </filter>
      </defs>
      <path d="M46 466 C 200 500, 400 540, 570 540 C 760 540, 980 480, 1148 388 L 1168 682 L 46 682 Z"
            fill="url(#bannerFill)" stroke="var(--yellow-edge)" stroke-width="5"
            stroke-linejoin="round" filter="url(#bannerShadow)"/>
    </svg>

    <h1 class="banner__title">BRIGHT SPARK ELECTRICAL PTY LTD</h1>
    <p class="banner__tagline">FREE QUOTES, FIXED PRICE, LIFETIME GUARENTEE</p>
  </main>
</body>
</html>
```